Investment online portal styling and design elements

We would like to design an online portal that our clients will use to access their personal investment information. Our business is Brenlow Investment Advisors (http://www.brenlowinvestmentadvisors.example/).

We are part of a large law firm and have been in business for 100 + years. Our clients are successful families who are seeking to manage their wealth in a diversified and global investment portfolio. We are preparing new investment reports and an accompanying online portal to present the investment information. This project is for the design and styling of the Summary page and Portfolio page (the style sheet and design elements for which can be transferred across the portal to all other pages) of a web portal that we have purchased from a vendor. The portal design should contain three content ideas: (1) that this is a Brenlow Investment Advisors Account Portal, (2) the name of the account and (3) the account number .

Proposals should assume HTML5 and CSS3 styling. We have determined that this portal should use menu-driven navigation. The menu should be presented consistently through the site and include:

1) Summary (which would include basic high level account details, like first page of the attached pdf)

2) Portfolio (which would include specifics into what the client’s assets are, in particular pages 2 and 3 of the attached pdf)

3) Performance

4) Holdings and Activity

5) Documents and Mail

6) My Profile

The content on each portal page will be controlled by the web portal technology we have purchased for this purpose.

RGB for the firm's colors are:
#33a6d7
#aaaaaa
#5c5c5c
#000000

Please refer to our website to see the design concepts used by the firm. I have attached the newly-designed set of client reports which we will introduce simultaneously with the portal. The charts, graphs, tables, etc. in these reports will be presented identically in the online portal. You should take into account our firm logo and the blue color, but you do not need to mimic the report design or the firm’s website design, although they should be able to coexist cohesively. We would like the portal to follow our overall, simple design ethic but reflect the fact that this is a fresh, new interface. I have also uploaded a pdf file of the final version of the first few pages of the reports. You can use the content in these pages for your design, if helpful. Thank you.

Target Market(s)

Clients who are investors

Industry/Entity Type

Financial Service

Coding

Coded - Design and coding required

Number of Pages Required

1 page

Font styles to use
Sans Serif

Requirements
Must have
• Clean, professional look and feel, menu-driven navigation (tabular or similar). Please see the project brief for RGB codes for our firm color palette.
Nice to have
• Please refer to sample of paper reports for overall look and feel. Not necessary to replicate exactly, but web portal should coexist with our paper reports and firm website.
Should not have
• No whimsy animated gifs, trendy over the top graphics. Must be conservatively clean and not gimmicky.

```html
<!DOCTYPE html>
<html lang="en">
<head>
<meta charset="utf-8">
<title>Brenlow Investment Advisors – Asset Allocation History</title>
<link href="https://fonts.googleapis.com/css2?family=Open+Sans:wght@400;600;700&display=swap" rel="stylesheet">
<style>
:root{
  --brand-blue:#33a6d7;
  --brand-grey:#aaaaaa;
  --brand-dark:#5c5c5c;
  --ink:#000000;
  --page-bg:#f1f1f1;
  --panel-border:#d9e0e8;
  --panel-head:#f7f8fa;
  --nav-text:#9a9a9a;
  --navy-text:#2b3a55;
}
*{box-sizing:border-box;margin:0;padding:0}
html,body{width:1200px;height:1036px;overflow:hidden}
body{background:var(--page-bg);font-family:"Open Sans",sans-serif;position:relative}
.page{position:absolute;left:99px;top:0;width:1003px;height:983px;background:#fff;box-shadow:0 0 3px rgba(0,0,0,.15)}
.topbar{height:49px;background:var(--brand-blue);color:#fff;font-weight:700;font-size:22px;text-align:center;line-height:49px;letter-spacing:.3px}
.site-header{position:relative;height:150px;border-bottom:1px solid #e6e6e6}
.brand{position:absolute;left:36px;top:50px;width:220px;display:flex;align-items:center;gap:10px}
.brand-square{flex:none;width:22px;height:22px;background:var(--brand-blue)}
.brand-name{font-size:14px;line-height:19px;font-weight:600;color:var(--brand-blue);letter-spacing:1px}
.brand-name span{display:block}
.main-nav{position:absolute;top:46px;left:0;width:100%}
.main-nav a{position:absolute;font-size:13px;color:var(--nav-text);text-decoration:none;white-space:nowrap}
.search-btn{position:absolute;left:929px;top:39px;width:32px;height:32px;border-radius:50%;background:#ececec}
.page-title{position:absolute;left:613px;top:95px;display:flex;align-items:center;gap:12px}
.page-title h1{font-size:22px;font-weight:600;color:var(--brand-blue);letter-spacing:.2px}
.content{position:absolute;left:36px;top:228px;width:930px}
.account-name{font-size:16px;color:var(--brand-blue);font-weight:600}
.account-number{font-size:12.5px;color:var(--brand-dark);margin-top:1px;padding-left:2px}
.section-title{margin-top:26px;font-size:23px;font-weight:600;color:var(--brand-dark)}
.section-title span{font-size:15px;color:var(--brand-blue)}
.chart-panel{position:absolute;left:0;top:136px;width:606px;height:498px;border:1px solid var(--panel-border)}
.chart-panel h2{height:34px;line-height:34px;padding-left:13px;background:var(--panel-head);border-bottom:1px solid #e8ecf0;font-size:14px;font-weight:600;color:var(--navy-text)}
.chart-panel svg{display:block}
.legend{position:absolute;left:686px;top:138px;list-style:none}
.legend li{font-size:11px;color:var(--brand-dark);height:20.6px;display:flex;align-items:center;gap:9px}
.legend i{width:9px;height:9px;display:inline-block}
.site-footer{position:absolute;left:0;top:926px;width:100%;height:57px;background:var(--brand-dark);color:#e6e6e6;text-align:center;line-height:57px;font-size:12px}
.site-footer strong{font-size:16px;font-weight:600;color:#fff;margin-right:3px}
</style>
</head>
<body>
<div class="page">
  <div class="topbar">BRENLOW INVESTMENT ADVISORS LLC</div>
  <header class="site-header">
    <div class="brand"><span class="brand-square"></span><span class="brand-name"><span>BRENLOW</span><span>INVESTMENT ADVISORS</span></span></div>
    <nav class="main-nav">
      <a style="left:289px">Investment Approach</a>
      <a style="left:444px">Our Team</a>
      <a style="left:531px">Market Intelligence</a>
      <a style="left:672px">in the Media</a>
      <a style="left:773px">Wealth Management</a>
    </nav>
    <svg class="search-btn" viewBox="0 0 32 32" aria-label="Search"><circle cx="16" cy="16" r="16" fill="#ececec"/><circle cx="14" cy="14" r="3.5" fill="none" stroke="#9a9a9a" stroke-width="1.6"/><line x1="16.5" y1="16.5" x2="21" y2="21" stroke="#9a9a9a" stroke-width="2"/></svg>
    <div class="page-title">
      <svg width="30" height="30" viewBox="0 0 30 30"><circle cx="15" cy="15" r="15" fill="#33a6d7"/><polygon points="12,9.5 20,15 12,20.5" fill="#fff"/></svg>
      <h1>ASSET ALLOCATION HISTORY</h1>
    </div>
  </header>

  <main class="content">
    <div class="account-name">Daniel Harper</div>
    <div class="account-number">Account number: 123456789</div>
    <div class="section-title">Asset Allocation History:<span>(as of March 31, 2015)</span></div>

    <section class="chart-panel">
      <h2>Asset Allocation History</h2>
      <svg width="604" height="462" viewBox="159 466 705 539" font-family="Arial, sans-serif">
        <g stroke="#fff" stroke-width="0.8">
          <polygon fill="#d00000" points="235,508 347,508 459,508 571,508 683,508 794,508 794,936 235,936"/>
          <polygon fill="#b2e04a" points="235,508.9 347,515.3 459,515.3 571,515.3 683,515.3 794,514.4 794,936 235,936"/>
          <polygon fill="#66d42e" points="235,510.1 347,531.5 459,534.5 571,535.8 683,541 794,538.8 794,936 235,936"/>
          <polygon fill="#d00000" points="235,576.5 347,595.7 459,597.9 571,602.2 683,597.9 794,606.4 794,936 235,936"/>
          <polygon fill="#e20000" points="235,757.5 347,778.5 459,783.6 571,780.6 683,779.8 794,778.5 794,936 235,936"/>
          <polygon fill="#ff2b2b" points="235,759.7 347,780.6 459,785.3 571,782.8 683,781.9 794,781.9 794,936 235,936"/>
          <polygon fill="#ff7700" points="235,762.7 347,784.1 459,788.3 571,786.2 683,784.9 794,784.9 794,936 235,936"/>
          <polygon fill="#ff7d0a" points="235,831.1 347,849.1 459,852.5 571,852.5 683,852.5 794,852.5 794,936 235,936"/>
          <polygon fill="#ffba1f" points="235,844 347,861.1 459,864.5 571,863.2 683,864.5 794,864.5 794,936 235,936"/>
          <polygon fill="#3f8b1e" points="235,873.9 347,891.1 459,893.2 571,893.2 683,893.2 794,891.1 794,936 235,936"/>
          <polygon fill="#1a5fd0" points="235,882.5 347,895.3 459,897.5 571,897.5 683,897.5 794,897.5 794,936 235,936"/>
          <polygon fill="#7b3fe4" points="235,891.1 347,903.9 459,906 571,906 683,906 794,906 794,936 235,936"/>
          <polygon fill="#c4c4c4" points="235,915.5 347,921.9 459,922.3 571,922.3 683,922.3 794,922.3 794,936 235,936"/>
          <polygon fill="#b388ff" points="235,924 347,925.3 459,925.3 571,925.3 683,925.3 794,925.3 794,936 235,936"/>
        </g>
        <g stroke="#000" stroke-width="1">
          <line x1="235" y1="508" x2="235" y2="936"/>
          <line x1="235" y1="936" x2="794" y2="936"/>
          <line x1="794" y1="508" x2="794" y2="936" stroke-width="0.6"/>
          <line x1="227" y1="508" x2="235" y2="508"/><line x1="227" y1="551" x2="235" y2="551"/>
          <line x1="227" y1="593" x2="235" y2="593"/><line x1="227" y1="636" x2="235" y2="636"/>
          <line x1="227" y1="679" x2="235" y2="679"/><line x1="227" y1="722" x2="235" y2="722"/>
          <line x1="227" y1="765" x2="235" y2="765"/><line x1="227" y1="807" x2="235" y2="807"/>
          <line x1="227" y1="850" x2="235" y2="850"/><line x1="227" y1="893" x2="235" y2="893"/>
          <line x1="347" y1="936" x2="347" y2="942"/><line x1="459" y1="936" x2="459" y2="942"/>
          <line x1="571" y1="936" x2="571" y2="942"/><line x1="683" y1="936" x2="683" y2="942"/>
          <line x1="794" y1="936" x2="794" y2="942"/>
        </g>
        <g font-size="11" fill="#222" text-anchor="end">
          <text x="224" y="512">100</text><text x="224" y="597">80</text>
          <text x="224" y="683">60</text><text x="224" y="769">40</text>
          <text x="224" y="854">20</text><text x="224" y="940">0</text>
        </g>
        <g font-size="11" fill="#222" text-anchor="middle">
          <text x="235" y="953">Oct-14</text><text x="347" y="953">Nov-14</text>
          <text x="459" y="953">Dec-14</text><text x="571" y="953">Jan-15</text>
          <text x="683" y="953">Feb-15</text><text x="794" y="953">Mar-15</text>
          <text x="515" y="974" font-weight="bold">Period</text>
          <text x="184" y="722" font-weight="bold" transform="rotate(-90 184 722)">% Allocation</text>
        </g>
      </svg>
    </section>

    <ul class="legend">
      <li><i style="background:#d00000"></i>Unconstrained Bonds</li>
      <li><i style="background:#b2e04a"></i>Cash</li>
      <li><i style="background:#b2e04a"></i>Equivalents</li>
      <li><i style="background:#66d42e"></i>Taxable Bonds</li>
      <li><i style="background:#d00000"></i>Common Stock</li>
      <li><i style="background:#e20000"></i>US Mid Capitalization</li>
      <li><i style="background:#ff2b2b"></i>US Small Capitalization</li>
      <li><i style="background:#ff7700"></i>International Developed</li>
      <li><i style="background:#ff7d0a"></i>International Small Cap</li>
      <li><i style="background:#ffba1f"></i>International Emerging</li>
      <li><i style="background:#3f8b1e"></i>International Bonds</li>
      <li><i style="background:#1a5fd0"></i>Emerging Markets Bonds</li>
      <li><i style="background:#7b3fe4"></i>Low Volatility Equities</li>
      <li><i style="background:#c4c4c4"></i>Commodities</li>
      <li><i style="background:#b388ff"></i>Frontier Markets</li>
    </ul>
  </main>

  <footer class="site-footer"><strong>Brenlow Investment Advisors LLC.</strong> ©2015 by Brenlow Investment Advisors LLC All Rights Reserved.Terms of usesite map</footer>
</div>
</body>
</html>
```